Penwick Insurance Post Card

Specializing in “Towing & Transportation Insurance”
See our website at http://penwickins-example.net/ for ideas on colors fonts etc.

Target Market(s)

Towing Companies

Font styles to use
Serif
Sans Serif

Requirements
Must have
• Specializing in “Towing & Transportation Insurance”
• Welcome to Penwick Insurance:
• 2nd sentence (With our Agency, we work to make ourselves available to your business for when you need us most to keep your business moving forward.)
• 3rd Sentence: (Our customers were in mind when developing our agency and will continue to find new ways to make doing business with us easier.)
• We Offer: Change “Dealers Physical Damage” to “Auto Dealer Liability” & “Garage Liability” to “Garage Repair Liability”
• Our address: 418 5th St NW, Suite B Decatur, AL 35602
• Email Address: PenwickInfo@velmorlink.example

```html
<!DOCTYPE html>
<html lang="en">
<head>
<meta charset="utf-8">
<title>Penwick Insurance Post Card</title>
<link rel="stylesheet" href="https://fonts.googleapis.com/css2?family=PT+Sans:wght@400;700&family=Arimo:ital,wght@1,700&family=Tinos:wght@700&display=swap">
<style>
  :root {
    --navy: #13294f;
    --blue: #0a4f9e;
    --blue-deep: #0b2a63;
    --gold: #b3904f;
    --panel: #f2f2f2;
    --text-grey: #6b6b6b;
    --line-grey: #cfcfcf;
    --stage: #ebebeb;
    --white: #ffffff;
  }
  * { box-sizing: border-box; margin: 0; padding: 0; }
  html, body { width: 951px; height: 1200px; overflow: hidden; }
  body { background: var(--stage); font-family: "PT Sans", sans-serif; position: relative; }

  .card {
    position: absolute; left: 81px; width: 725px;
    background: var(--white);
    box-shadow: 0 3px 8px rgba(0,0,0,.25);
    overflow: hidden;
  }
  .card--front { top: 70px; height: 525px; background: var(--panel); }
  .card--back { top: 630px; height: 523px; }
  .card__art { position: absolute; inset: 0; }
  .card > *:not(.card__art) { position: absolute; }

  .brand { width: 284px; text-align: center; color: var(--navy); font-family: "PT Sans", sans-serif; font-weight: 400; }
  .brand__name { display: block; font-size: 44px; line-height: 44px; letter-spacing: 6px; padding-left: 6px; }
  .brand__sub { display: block; font-size: 16px; line-height: 18px; letter-spacing: 15px; padding-left: 15px; margin-top: 8px; }
  .brand__tagline { display: block; margin-top: 11px; font-family: "Arimo", sans-serif; font-style: italic; font-weight: 700; font-size: 9.6px; line-height: 12px; color: var(--gold); white-space: nowrap; }

  .welcome { font-family: "PT Sans", sans-serif; font-weight: 400; font-size: 17px; letter-spacing: -0.2px; color: var(--navy); white-space: nowrap; }
  .intro { font-size: 15.8px; line-height: 18px; color: var(--text-grey); width: 318px; }
  .intro p + p { margin-top: 10px; }

  .offer-tab {
    left: 0; top: 364px; width: 156px; height: 34px;
    background: linear-gradient(90deg, var(--blue), var(--blue-deep));
    border-radius: 0 12px 12px 0; box-shadow: 2px 2px 3px rgba(0,0,0,.25);
    color: var(--white); font-size: 17px;
    line-height: 34px; padding-left: 26px;
  }
  .offer-list { list-style: none; left: 20px; top: 406px; }
  .offer-list li { display: flex; align-items: center; gap: 10px; font-weight: 700; font-size: 17.5px; color: var(--navy); height: 25px; }
  .offer-list svg { width: 13px; height: 13px; flex: none; }

  .web { color: var(--white); font-size: 16px; white-space: nowrap; }
  .call { font-family: "Tinos", serif; font-weight: 700; font-size: 21px; color: var(--white); white-space: nowrap; }

  .back-band-title { left: 0; top: 136px; width: 374px; text-align: center; color: var(--white); font-weight: 400; font-size: 17px; letter-spacing: -0.2px; line-height: 46px; }
  .back-contact { left: 0; top: 424px; width: 324px; text-align: center; color: var(--white); }
  .back-contact .call { display: block; margin-bottom: 8px; }
  .back-contact .line { display: block; font-size: 16px; line-height: 25px; }

  .mail-address { left: 408px; top: 23px; font-size: 14.5px; line-height: 22px; color: var(--navy); font-style: normal; }
  .stamp-box { left: 596px; top: 24px; width: 98px; height: 66px; border: 2px solid var(--line-grey); }
  .address-lines { left: 408px; top: 197px; width: 286px; }
  .address-lines span { display: block; height: 33px; border-top: 2px solid var(--line-grey); }
</style>
</head>
<body>

<section class="card card--front">
  <svg class="card__art" width="725" height="525" viewBox="0 0 725 525">
    <defs>
      <linearGradient id="frontBlue" x1="0" x2="1" y1="0" y2="0">
        <stop offset="0" stop-color="#0a56a8"/>
        <stop offset="1" stop-color="#0b2a63"/>
      </linearGradient>
      <linearGradient id="frontPhoto" x1="0" x2="1" y1="0" y2="1">
        <stop offset="0" stop-color="#c9ccd0"/>
        <stop offset=".55" stop-color="#8f8f8c"/>
        <stop offset="1" stop-color="#b9b6ae"/>
      </linearGradient>
    </defs>
    <path d="M345 0 C335 170 380 320 470 395 L380 410 C330 330 318 170 330 0 Z" fill="#dcdcdc"/>
    <path role="img" aria-label="Photo of a tow truck lifting a silver car on a city street"
          d="M358 0 L725 0 L725 372 C620 378 530 388 455 398 C385 330 350 190 358 0 Z" fill="url(#frontPhoto)"/>
    <path d="M120 525 C300 430 520 392 725 366 L725 380 C520 405 320 445 160 525 Z" fill="var(--white)"/>
    <path d="M140 525 C320 438 530 396 725 370" fill="none" stroke="var(--gold)" stroke-width="4"/>
    <path d="M150 525 C330 444 540 402 725 378 L725 525 Z" fill="url(#frontBlue)"/>
    <circle role="img" aria-label="Photo of a silver sedan being hooked up for towing" cx="629" cy="360" r="76" fill="#a9aca8" stroke="var(--gold)" stroke-width="4"/>
  </svg>

  <div class="brand" style="left:19px;top:48px;">
    <span class="brand__name">PENWICK</span>
    <span class="brand__sub">INSURANCE</span>
    <span class="brand__tagline">Specializing in Towing &amp; Transportation Insurance</span>
  </div>

  <h1 class="welcome" style="left:24px;top:178px;">WELCOME TO PENWICK INSURANCE</h1>
  <div class="intro" style="left:19px;top:207px;">
    <p>With our Agency, we work to make ourselves available to your business for when you need us most to keep your business moving forward.</p>
    <p>Our customers were in mind when developing our agency and will continue to find new ways to make doing business with us easier.</p>
  </div>

  <div class="offer-tab">WE OFFER</div>
  <ul class="offer-list">
    <li><svg viewBox="0 0 13 13"><circle cx="6.5" cy="6.5" r="6.5" fill="var(--gold)"/><path d="M5 3.8 L7.8 6.5 L5 9.2" fill="none" stroke="#fff" stroke-width="1.6"/></svg>Auto Dealer Liability</li>
    <li><svg viewBox="0 0 13 13"><circle cx="6.5" cy="6.5" r="6.5" fill="var(--gold)"/><path d="M5 3.8 L7.8 6.5 L5 9.2" fill="none" stroke="#fff" stroke-width="1.6"/></svg>Garage Repair Liability</li>
  </ul>

  <div class="web" style="right:27px;top:456px;">www.penwickins-example.net</div>
  <div class="call" style="right:22px;top:483px;">Call us Today: 334-555-0187</div>
</section>

<section class="card card--back">
  <svg class="card__art" width="725" height="523" viewBox="0 0 725 523">
    <defs>
      <clipPath id="backPanel">
        <path d="M0 0 L345 0 C373 150 383 330 333 523 L0 523 Z"/>
      </clipPath>
      <linearGradient id="backBlue" x1="0" x2="1" y1="0" y2="0">
        <stop offset="0" stop-color="#0a56a8"/>
        <stop offset="1" stop-color="#0b2a63"/>
      </linearGradient>
      <linearGradient id="backPhoto" x1="0" x2="0" y1="0" y2="1">
        <stop offset="0" stop-color="#c4ccd6"/>
        <stop offset=".45" stop-color="#8e8c88"/>
        <stop offset="1" stop-color="#a8a29a"/>
      </linearGradient>
    </defs>
    <path d="M355 0 C385 150 395 330 345 523 L360 523 C408 330 398 150 368 0 Z" fill="#d6d6d6"/>
    <g clip-path="url(#backPanel)">
      <rect x="0" y="136" width="400" height="46" fill="var(--gold)"/>
      <rect role="img" aria-label="Photo of a flatbed tow truck carrying a car in front of mountains" x="0" y="182" width="400" height="233" fill="url(#backPhoto)"/>
      <rect x="0" y="415" width="400" height="108" fill="url(#backBlue)"/>
    </g>
    <path d="M345 0 C373 150 383 330 333 523" fill="none" stroke="var(--gold)" stroke-width="5"/>
    <circle role="img" aria-label="Photo of a dark sedan loaded on a tow truck bed" cx="351" cy="378" r="56" fill="#6f7784" stroke="var(--gold)" stroke-width="4"/>
  </svg>

  <div class="brand" style="left:37px;top:28px;">
    <span class="brand__name">PENWICK</span>
    <span class="brand__sub">INSURANCE</span>
    <span class="brand__tagline">Specializing in Towing &amp; Transportation Insurance</span>
  </div>

  <h2 class="back-band-title">WELCOME TO PENWICK INSURANCE</h2>

  <div class="back-contact">
    <span class="call">Call us Today: 334-555-0187</span>
    <span class="line">PenwickInfo@velmorlink.example</span>
    <span class="line">www.penwickins-example.net</span>
  </div>

  <address class="mail-address">Penwick Insurance<br>418 5th St NW<br>Decatur, AL 35602</address>
  <div class="stamp-box"></div>
  <div class="address-lines"><span></span><span></span><span></span><span></span></div>
</section>

</body>
</html>
```